Irrigation Business needs their business cards modernised and revamped

I would like to keep my current logo, colours and revamp the format of the card.

I would like the card to be clean yet important.

Im not sure if you include texture but i would like the named logo to be indented into the card etc.

show me something alive and free something thats clinical to the point yet has a feel of achievement. i would like people to go nice card.

Target Market(s)

high end clients, corporate, sports field manger, the guys that make the decisions

Industry/Entity Type

Business

Contact Information for Business Card

nformation to be included

Dorian Hesk (Director)
0487253916
dorian@tfcraft.biz
www.taddsfieldcrafts.com

instagram logo
google logo
facebook logo

Colors

Designer to choose colors to be used in the design.

Requirements
Nice to have
• indentations a really nice feel to the card good texture

```html
<!DOCTYPE html>
<html lang="en">
<head>
<meta charset="utf-8">
<title>Tadd's Field Crafts – Business Card</title>
<link rel="stylesheet" href="https://fonts.googleapis.com/css2?family=Open+Sans:wght@400;700;800&display=swap">
<style>
  :root {
    --backdrop: #1d1d1d;
    --paper: #f4f4f2;
    --blue-deep: #2b62ac;
    --blue-light: #2f9fd3;
    --blue-ink: #2a5fa8;
    --green: #1f9a4f;
    --grey-text: #555555;
    --white: #ffffff;
  }
  * { box-sizing: border-box; margin: 0; padding: 0; }
  html, body {
    width: 960px; height: 1200px; overflow: hidden;
    background: var(--backdrop);
    font-family: "Open Sans", Arial, sans-serif;
  }
  .canvas {
    position: relative; width: 960px; height: 1200px;
  }
  .card {
    position: absolute; left: 130px;
    width: 700px; height: 400px;
    border-radius: 28px;
    background: var(--paper);
    overflow: hidden;
    box-shadow: 0 10px 30px rgba(0,0,0,.5);
  }
  .card--front { top: 140px; }
  .card--back { top: 680px; }

  /* Front */
  .brand {
    position: absolute; inset: 0;
    display: flex; flex-direction: column; align-items: center; justify-content: center;
    gap: 22px;
  }
  .brand__dot {
    width: 110px; height: 110px; border-radius: 50%;
    background: var(--blue-light);
  }
  .brand__name {
    font-weight: 800; font-size: 40px; letter-spacing: .5px;
    color: var(--blue-ink); text-transform: uppercase;
  }

  /* Back */
  .back__waves { position: absolute; inset: 0; }
  .holder {
    position: absolute; left: 60px; top: 62px;
  }
  .holder__name {
    font-weight: 800; font-size: 30px; color: var(--green);
    text-transform: uppercase; line-height: 1.1;
  }
  .holder__role {
    font-size: 22px; color: var(--grey-text); line-height: 1.2;
  }
  .back__brand {
    position: absolute; left: 500px; top: 40px; width: 170px;
    display: flex; flex-direction: column; align-items: center; gap: 10px;
  }
  .back__brand .brand__dot { width: 100px; height: 100px; }
  .back__brand .brand__name { font-size: 16px; letter-spacing: .3px; }
  .contact {
    position: absolute; left: 50px; top: 268px;
    list-style: none; color: var(--white); font-size: 18px;
  }
  .contact li { display: flex; align-items: center; gap: 14px; height: 32px; }
  .contact svg { width: 18px; height: 18px; flex: none; }
  .social {
    position: absolute; right: 60px; bottom: 28px;
    display: flex; gap: 16px;
  }
  .social__dot {
    width: 38px; height: 38px; border-radius: 50%; background: var(--white);
  }
</style>
</head>
<body>
<main class="canvas">

  <section class="card card--front" aria-label="Card front">
    <div class="brand">
      <span class="brand__dot"></span>
      <span class="brand__name">Tadd's Field Crafts</span>
    </div>
  </section>

  <section class="card card--back" aria-label="Card back">
    <svg class="back__waves" viewBox="0 0 700 400" preserveAspectRatio="none" aria-hidden="true">
      <path d="M0,205 C210,170 430,330 700,285 L700,400 L0,400 Z" fill="var(--blue-light)"/>
      <path d="M0,228 C210,193 430,356 700,312 L700,400 L0,400 Z" fill="var(--blue-deep)"/>
      <path d="M0,226 C210,191 430,354 700,310" fill="none" stroke="var(--white)" stroke-width="2"/>
    </svg>

    <div class="holder">
      <p class="holder__name">Dorian Hesk</p>
      <p class="holder__role">Director</p>
    </div>

    <div class="back__brand">
      <span class="brand__dot"></span>
      <span class="brand__name">Tadd's Field Crafts</span>
    </div>

    <ul class="contact">
      <li>
        <svg viewBox="0 0 18 18"><rect x="4" y="1" width="10" height="16" rx="2" fill="none" stroke="#fff" stroke-width="1.6"/><circle cx="9" cy="14" r="1" fill="#fff"/></svg>
        048 725 3916
      </li>
      <li>
        <svg viewBox="0 0 18 18"><rect x="1" y="4" width="16" height="11" fill="#fff"/><path d="M1,4 L9,10 L17,4" fill="none" stroke="#2b62ac" stroke-width="1.4"/></svg>
        dorian@tfcraft.biz
      </li>
      <li>
        <svg viewBox="0 0 18 18"><circle cx="9" cy="9" r="7.5" fill="none" stroke="#fff" stroke-width="1.5"/><ellipse cx="9" cy="9" rx="3.2" ry="7.5" fill="none" stroke="#fff" stroke-width="1.3"/><path d="M1.5,9 H16.5 M3,5 H15 M3,13 H15" stroke="#fff" stroke-width="1.2"/></svg>
        www.taddsfieldcrafts.com
      </li>
    </ul>

    <div class="social" aria-label="Social channels">
      <span class="social__dot"></span>
      <span class="social__dot"></span>
      <span class="social__dot"></span>
    </div>
  </section>

</main>
</body>
</html>
```